Website for Dental Office - The Bright Harbor Clinic

The bright harbor clinic is a dental office offering cosmetic dentistry, general dentistry, and multi-specialty dental care all under one roof in our state-of-the-art cosmetic dental center. We are particularly striving to provide services that fit the need of the young generation. Thus, we hope to have a modern, professional concise website that represents our spirit.

*Should be able to switch from English to Chinese

6 sections besides homepage:
Home, Meet us, Services,
Patient Info, Cases&Reviews, Blog, Contact

The Services sections should contain multiple subsections such as cleaning and prevention, cosmetic dentistry, implant dentistry, removable dentures, etc...
The Patient Info section is also intended to contain several subsections such as
New Patient offer, accepted Insurance, patient portal, helpful tips, etc...

Target Market(s)

young generation

Coding

Coded - Design and coding required

Number of Pages Required

5+ page

Font styles to use
Sans Serif

Colors
0592cd
33a6d7
85cae6
00a990
33b8a4
86cfc6
cee9f5
cfeae6
3277b5

Requirements
Must have
• *Should be able to switch from English to Chinese
Nice to have
• http://www.thebrightharborclinic.example/
• As a reference, the above link is the current website, but we would like to change the appearance and the content (our new logo's picture is attached)

```html
<!DOCTYPE html>
<html lang="en">
<head>
<meta charset="utf-8">
<title>The Bright Harbor Clinic</title>
<link href="https://fonts.googleapis.com/css2?family=Montserrat:wght@300;400;500;600;700&family=Lato:wght@400;700&display=swap" rel="stylesheet">
<style>
:root{
  --blue:#0592cd;--blue-2:#33a6d7;--blue-3:#85cae6;--blue-deep:#3277b5;
  --teal:#00a990;--teal-2:#33b8a4;--teal-3:#86cfc6;
  --ice:#cee9f5;--mint:#cfeae6;
  --ink:#1c1c1c;--text:#333;--muted:#666;--line:#e3e3e3;
}
*{box-sizing:border-box;margin:0;padding:0}
html,body{width:1200px;height:4161px;overflow:hidden}
body{font-family:'Lato',sans-serif;color:var(--text);background:#fff;position:relative}
a{color:inherit;text-decoration:none}
.abs{position:absolute}
.h-title{font-family:'Montserrat',sans-serif;font-weight:400;color:var(--ink);font-size:36px;letter-spacing:-.3px;white-space:nowrap}
.h-title b{color:var(--blue);font-weight:600}
.btn{display:inline-flex;align-items:center;gap:9px;height:49px;padding:0 32px;border-radius:25px;color:#fff;font-weight:700;font-size:17px;font-family:'Lato',sans-serif;white-space:nowrap}
.btn-blue{background:var(--blue)}
.btn-teal{background:var(--teal)}
.btn .arr{width:16px;height:16px;border-radius:50%;background:#fff;display:inline-block;position:relative}
.btn .arr::after{content:"";position:absolute;left:5px;top:4px;border-top:4px solid transparent;border-bottom:4px solid transparent;border-left:6px solid var(--blue)}
.btn-teal .arr::after{border-left-color:var(--teal)}
.para{font-size:15px;line-height:36px;color:var(--ink)}

/* top bar */
.topbar{left:0;top:0;width:1200px;height:42px;background:var(--blue);color:#fff;font-size:14px}
.topbar .mail{left:90px;top:0;height:42px;display:flex;align-items:center;gap:6px;padding-right:12px;border-right:1px solid rgba(255,255,255,.3)}
.topbar .right{right:90px;top:0;height:42px;display:flex;font-size:13px}
.topbar .right span{display:flex;align-items:center;padding:0 12px;border-left:1px solid rgba(255,255,255,.3)}
.topbar .right span:last-child{border-right:1px solid rgba(255,255,255,.3)}

/* header */
.header{left:0;top:42px;width:1200px;height:111px;background:#fff}
.call{left:100px;top:30px;display:flex;gap:12px;align-items:center}
.call small{display:block;color:var(--blue);font-size:14px}
.call strong{font-size:17px;color:var(--ink)}
.brand{display:flex;align-items:center;gap:18px}
.header .brand{left:460px;top:24px}
.brand .mark{width:56px;height:56px;background:var(--blue-2);border-radius:8px;flex:none}
.brand .name{font-family:'Montserrat',sans-serif;font-weight:600;color:var(--blue);font-size:24px;line-height:28px;width:230px;text-transform:uppercase}
.social{right:90px;top:34px;display:flex;gap:10px}
.social i{width:41px;height:41px;border-radius:50%;background:var(--teal);display:block}

/* nav */
.nav{left:0;top:153px;width:1200px;height:65px;background:#f1f1f1;border-top:1px solid var(--line);display:flex;justify-content:center;align-items:center;gap:45px;font-size:20px;color:var(--ink)}
.nav a.active{color:var(--teal);font-weight:700}

/* hero */
.hero{left:0;top:218px;width:1200px;height:622px;overflow:hidden}
.hero .photo{position:absolute;inset:0;background:linear-gradient(100deg,#f4f6f8 0%,#e6ecf1 40%,#c9d5e2 70%,#eef1f4 100%)}
.hero h1{left:84px;top:170px;font-family:'Montserrat',sans-serif;font-weight:600;font-size:56px;color:var(--blue-2);white-space:nowrap}
.hero p{left:89px;top:246px;font-size:17px;line-height:36px;font-weight:700;color:#111;width:520px}
.hero .btn{left:89px;top:329px;height:48px;padding:0 26px}
.hero svg.wave{position:absolute;left:0;bottom:0}

/* welcome */
.welcome{left:0;top:900px;width:1200px;text-align:center}
.welcome .para{width:980px;margin:22px auto 0}
.welcome .btns{margin-top:36px;display:flex;justify-content:center;gap:12px}
.divider{left:89px;width:1022px;height:1px;background:var(--line)}

/* about */
.circle{border-radius:50%;border:6px solid var(--teal);padding:8px;background:#fff}
.circle .img{width:100%;height:100%;border-radius:50%}
.about-img{left:68px;top:1308px;width:446px;height:446px}
.about-text{left:547px;top:1376px;width:563px}
.about-text .para{margin-top:14px;text-align:justify}
.about-text .btn{margin-top:22px}

/* services */
.services{left:0;top:1833px;width:1200px;height:703px}
.services .title{left:0;top:142px;width:1200px;text-align:center;color:#fff;font-family:'Montserrat',sans-serif;font-size:36px;font-weight:300}
.services .title b{font-weight:700}
.services .lead{left:140px;top:205px;width:920px;text-align:center;color:#fff;font-size:15px;line-height:36px}
.card{top:305px;width:323px;height:193px;background:#fff}
.card .img{height:158px}
.card .cap{height:35px;background:var(--teal-2);color:#fff;font-weight:700;font-size:15px;display:flex;align-items:center;justify-content:center}
.card.active .img{height:193px}
.card.active .overlay{position:absolute;left:22px;top:14px;right:22px;bottom:14px;background:rgba(0,169,144,.85);border:1px dashed rgba(255,255,255,.6);color:#fff;display:flex;flex-direction:column;align-items:center;justify-content:center;gap:4px}
.card.active .overlay strong{font-family:'Montserrat',sans-serif;font-weight:500;font-size:23px}
.card.active .overlay span{font-size:15px}
.dots{display:flex;gap:13px;justify-content:center}
.dots i{width:15px;height:15px;border:2px solid currentColor;border-radius:50%;display:block;position:relative}
.dots i.on::after{content:"";position:absolute;left:3px;top:3px;width:5px;height:5px;border-radius:50%;background:currentColor}

/* patient info */
.pi-text{left:86px;top:2678px;width:567px}
.pi-text .para{margin-top:12px;text-align:justify}
.pi-text .btns{margin-top:22px;display:flex;gap:14px}
.pi-img{left:689px;top:2615px;width:446px;height:446px}

/* reviews */
.reviews{left:0;top:3195px;width:1200px;text-align:center}
.quote{font-family:Georgia,serif;font-size:90px;line-height:60px;color:var(--blue-2);height:56px;margin-top:14px;font-weight:700}
.stars{color:#f4a521;font-size:22px;letter-spacing:2px;margin-top:6px}
.reviews .para{width:840px;margin:6px auto 0;color:var(--muted)}
.reviews .who{font-family:'Montserrat',sans-serif;font-weight:500;color:var(--teal);font-size:27px;margin-top:12px}
.reviews .dots{color:var(--teal);margin-top:14px}

/* footer */
.footer{left:0;top:3577px;width:1200px;height:584px;overflow:hidden;color:#fff}
.footer .bg{position:absolute;inset:0;background:linear-gradient(160deg,#2a3438 0%,#1d262a 55%,#263035 100%)}
.footer .brand{left:0;top:132px;width:1200px;justify-content:center}
.footer .brand .mark{width:82px;height:82px;background:var(--blue-3)}
.footer .brand .name{font-size:38px;line-height:46px;width:auto;color:var(--blue-2);font-weight:500;white-space:nowrap}
.contact{top:267px;width:340px;text-align:center;font-size:17px;line-height:28px}
.contact .ic{width:84px;height:84px;border-radius:50%;background:var(--teal);margin:0 auto 14px;display:flex;align-items:center;justify-content:center}
.flinks{left:0;top:436px;width:1200px;text-align:center;font-size:15px;line-height:20px;font-weight:700}
.flinks span{margin:0 7px;font-weight:400}
.copy{left:0;top:476px;width:1200px;text-align:center;font-size:14px;line-height:20px}
.fsocial{left:0;top:514px;width:1200px;display:flex;justify-content:center;gap:6px}
.fsocial i{width:30px;height:30px;border-radius:50%;border:2px solid #fff;display:block}
</style>
</head>
<body>

<div class="abs topbar">
  <div class="abs mail">
    <svg width="15" height="11" viewBox="0 0 15 11"><rect x=".5" y=".5" width="14" height="10" fill="#fff"/><path d="M1 1l6.5 5L14 1" stroke="#0592cd" fill="none"/></svg>
    info@thebrightharborclinic.example
  </div>
  <div class="abs right"><span>Patient Portal</span><span>EN ▾</span></div>
</div>

<header class="abs header">
  <div class="abs call">
    <svg width="42" height="42" viewBox="0 0 42 42"><circle cx="21" cy="21" r="19" fill="none" stroke="#00a990" stroke-width="2.5"/><path d="M14 12c2-1 3 0 4 3s-2 3-1 5 3 5 5 6 2-2 5-1 4 2 3 4-3 3-6 2-10-7-11-12 0-6 1-7z" fill="#00a990"/></svg>
    <div><small>Call us:</small><strong>+1-555-014-7720</strong></div>
  </div>
  <div class="abs brand"><span class="mark"></span><span class="name">The Bright Harbor Clinic</span></div>
  <div class="abs social"><i></i><i></i><i></i><i></i></div>
</header>

<nav class="abs nav">
  <a class="active">Home</a><a>Meet Us</a><a>Our Services</a><a>Patient Info</a><a>Cases &amp; Reviews</a><a>Blog</a><a>Contact</a>
</nav>

<section class="abs hero">
  <div class="photo" role="img" aria-label="Smiling patient reclining in a dental chair in a bright clinic"></div>
  <h1 class="abs">The Bright Harbor Clinic</h1>
  <p class="abs">Lorem ipsum dolor sit amet, consectetur adipiscing elit, sed do eiusmod tempor incididunt aliqua.</p>
  <a class="abs btn btn-teal">
    <svg width="17" height="17" viewBox="0 0 17 17"><path d="M16 1L1 8l5 2 1 6 3-4 4 3z" fill="#fff"/></svg>
    Helpful Tips</a>
  <svg class="wave" width="1200" height="70" viewBox="0 0 1200 70" preserveAspectRatio="none">
    <path d="M0 44C200 2 420 -2 640 30 860 62 1060 66 1200 38V70H0Z" fill="#fff"/>
    <path d="M0 40C200 -2 420 -6 640 28 780 48 900 56 1000 56" fill="none" stroke="#00a990" stroke-width="5"/>
  </svg>
</section>

<section class="abs welcome">
  <h2 class="h-title">Welcome to <b>The Bright Harbor Clinic</b></h2>
  <p class="para">Sed ut perspiciatis unde omnis iste natus error sit voluptatem accusantium doloremque laudantium, totam rem aperiam, eaque ipsa quae ab illo inventore veritatis et quasi architecto beatae vitae dicta sunt explicabo. Nemo enim ipsam &nbsp;aspernatur aut odit aut fugit, sed quia consequuntur magni dolores eos qui ratione voluptatem sequi nesciunt.</p>
  <div class="btns"><a class="btn btn-blue">Read More <i class="arr"></i></a><a class="btn btn-teal">Contact Us <i class="arr"></i></a></div>
</section>

<div class="abs divider" style="top:1230px"></div>

<div class="abs circle about-img"><div class="img" role="img" aria-label="Portrait of a smiling woman in a winter hat" style="background:radial-gradient(circle at 50% 55%,#e8b894,#b77a4e 60%,#6e4a2e)"></div></div>
<section class="abs about-text">
  <h2 class="h-title">About <b>The Bright Harbor Clinic</b></h2>
  <p class="para">Sed ut perspiciatis unde omnis iste natus error sit voluptatem accusantium doloremque laudantium, totam rem aperiam, eaque ipsa quae ab illo inventore veritatis et quasi architecto beatae vitae dicta sunt explicabo. Nemo enim ipsam voluptatem quia voluptas sit aspernatur aut odit aut fugit, sed &nbsp;eos qui ratione voluptatem sequi nesciunt.</p>
  <a class="btn btn-teal">Read More <i class="arr"></i></a>
</section>

<section class="abs services">
  <svg class="abs" style="left:0;top:0" width="1200" height="703" viewBox="0 0 1200 703" preserveAspectRatio="none" role="img" aria-label="Teal and blue band over a faint clinic scene">
    <defs><linearGradient id="svcGrad" x1="0" y1="0" x2="0" y2="1"><stop offset="0" stop-color="#00a990"/><stop offset=".55" stop-color="#1a9cb5"/><stop offset="1" stop-color="#0592cd"/></linearGradient></defs>
    <path d="M0 30C260 80 560 70 820 38 1000 16 1120 6 1200 0V640C1000 600 760 610 520 650 300 686 120 700 0 703Z" fill="url(#svcGrad)"/>
    <path d="M900 30C1020 14 1130 4 1200 2" fill="none" stroke="#00a990" stroke-width="5"/>
    <path d="M0 690C160 675 300 660 420 650" fill="none" stroke="#00a990" stroke-width="6"/>
  </svg>
  <h2 class="abs title">Our <b>Services</b></h2>
  <p class="abs lead">Sed ut perspiciatis unde omnis iste natus error sit voluptatem accusantium doloremque laudantium, totam rem aperiam, eaque ipsa quae ab illo inventore veritatis et quasi architecto beatae vitae dicta sunt explicabo.</p>
  <div class="abs card" style="left:98px"><div class="img" role="img" aria-label="Dentist cleaning a patient's teeth" style="background:linear-gradient(120deg,#2c3f8f,#5a6fb8 55%,#d9a59a)"></div><div class="cap">Cleaning and Prevention</div></div>
  <div class="abs card active" style="left:439px"><div class="img" role="img" aria-label="Dentist explaining an implant to a patient" style="background:linear-gradient(120deg,#cfd8dc,#9fb3bb)"></div><div class="overlay"><strong>Implant Dentistry</strong><span>Read More ➔</span></div></div>
  <div class="abs card" style="left:778px"><div class="img" role="img" aria-label="Dentist treating a patient in a modern surgery" style="background:linear-gradient(120deg,#dfe7ee,#b8c7d4 60%,#e5a3c0)"></div><div class="cap">Removable Dentures</div></div>
  <div class="abs dots" style="left:0;top:539px;width:1200px;color:#fff"><i></i><i class="on"></i><i></i></div>
</section>

<section class="abs pi-text">
  <h2 class="h-title">Patient <b>Info</b></h2>
  <p class="para">Sed ut perspiciatis unde omnis iste natus error sit voluptatem accusantium doloremque laudantium, totam rem aperiam, eaque ipsa quae ab illo inventore veritatis et quasi architecto beatae vitae dicta sunt explicabo. Nemo enim ipsam voluptatem quia voluptas sit aspernatur aut odit aut fugit, sed &nbsp;eos qui ratione voluptatem sequi nesciunt.</p>
  <div class="btns"><a class="btn btn-blue">Read More <i class="arr"></i></a><a class="btn btn-teal">New Patient Offer <i class="arr"></i></a></div>
</section>
<div class="abs circle pi-img"><div class="img" role="img" aria-label="Dental assistant scanning a patient's teeth beside a monitor" style="background:radial-gradient(circle at 60% 50%,#cfe0d6,#9fb8ad 60%,#7d8f98)"></div></div>

<div class="abs divider" style="top:3136px"></div>

<section class="abs reviews">
  <h2 class="h-title">Cases &amp; <b>Reviews</b></h2>
  <div class="quote">“</div>
  <div class="stars">★★★★★</div>
  <p class="para">Sed ut perspiciatis unde omnis iste natus error sit voluptatem accusantium doloremque laudantium, totam rem aperiam, eaque ipsa quae ab illo inventore &nbsp;explicabo.</p>
  <div class="who">Daniel Reyes</div>
  <div class="dots"><i></i><i class="on"></i><i></i></div>
</section>

<footer class="abs footer">
  <div class="bg" role="img" aria-label="Dim background of a dentist at work"></div>
  <svg class="abs" style="left:0;top:0" width="1200" height="60" viewBox="0 0 1200 60" preserveAspectRatio="none">
    <path d="M0 0H1200V14C1000 40 760 52 560 40 360 28 160 14 0 26Z" fill="#fff"/>
    <path d="M390 6C560 40 820 44 1000 34 1100 28 1160 20 1200 14" fill="none" stroke="#00a990" stroke-width="5"/>
  </svg>
  <div class="abs brand"><span class="mark"></span><span class="name">THE BRIGHT HARBOR<br>CLINIC</span></div>
  <div class="abs contact" style="left:129px">
    <div class="ic"><svg width="40" height="44" viewBox="0 0 40 44"><path d="M20 4a11 11 0 0 1 11 11c0 9-11 20-11 20S9 24 9 15A11 11 0 0 1 20 4z" fill="none" stroke="#fff" stroke-width="2"/><circle cx="20" cy="15" r="4" fill="none" stroke="#fff" stroke-width="2"/><path d="M6 40h28" stroke="#fff" stroke-width="2"/></svg></div>
    27 Harbor Lane, Suite 210<br>Fairview, MA 02100
  </div>
  <div class="abs contact" style="left:426px">
    <div class="ic"><svg width="40" height="40" viewBox="0 0 40 40"><path d="M9 6c3-2 5 0 7 5s-3 5-2 8 5 8 8 9 3-4 8-2 6 3 4 6-5 5-10 3S9 25 7 16C6 11 7 7 9 6z" fill="none" stroke="#fff" stroke-width="2"/></svg></div>
    Phone:<br>1-555-014-7720
  </div>
  <div class="abs contact" style="left:736px">
    <div class="ic"><svg width="44" height="32" viewBox="0 0 44 32"><rect x="2" y="2" width="40" height="28" fill="none" stroke="#fff" stroke-width="2"/><path d="M2 2l20 16L42 2M2 30l15-14M42 30L27 16" fill="none" stroke="#fff" stroke-width="2"/></svg></div>
    Email:<br>info@thebrightharborclinic.example
  </div>
  <div class="abs flinks">Home<span>|</span>Meet Us<span>|</span>Services<span>|</span>Patient Info<span>|</span>Cases &amp; Reviews<span>|</span>Blog<span>|</span>Contact</div>
  <div class="abs copy">© 2019 Company Name &nbsp;All right reserved</div>
  <div class="abs fsocial"><i></i><i></i><i></i><i></i></div>
</footer>

</body>
</html>
```